Business Card Design

Lawn service

Industry/Entity Type

Business

Contact Information for Business Card

Fern Hollow Lawn & Garden , deborah finch/owner,operater,2184 wexley millrd.. e. cedarvale,tn. 38472, phone:555-555-0147, Residential,Commercial, Lawn and Landscape Maintenance, Bushhogging

```html
<!DOCTYPE html>
<html lang="en">
<head>
<meta charset="utf-8">
<title>Fern Hollow Lawn &amp; Garden — Business Card</title>
<link href="https://fonts.googleapis.com/css2?family=Andika:wght@400;700&display=swap" rel="stylesheet">
<style>
  :root {
    --page: #ecebe6;
    --card-dark: #0f4a23;
    --card-mid: #1d6b2f;
    --swoosh-light: #9fd157;
    --swoosh-mid: #5fae36;
    --text-white: #ffffff;
    --text-lime: #a8dc4c;
    --text-yellow: #d9ec63;
    --grass-top: #4f9a34;
    --grass-bottom: #2c7a2b;
    --footer-text: #0d3a1a;
  }
  html, body {
    margin: 0;
    width: 1200px;
    height: 900px;
    overflow: hidden;
    background: var(--page);
    font-family: "Andika", "Trebuchet MS", sans-serif;
  }
  .card {
    position: absolute;
    left: 100px;
    top: 165px;
    width: 1000px;
    height: 570px;
    border-radius: 6px;
    overflow: hidden;
    background: radial-gradient(ellipse at 55% 40%, var(--card-mid), var(--card-dark) 75%);
    box-shadow: 0 12px 30px rgba(0,0,0,.25);
  }
  .card__shapes {
    position: absolute;
    inset: 0;
  }
  .brand {
    position: absolute;
    left: 120px;
    top: 170px;
    width: 320px;
    display: flex;
    align-items: center;
    gap: 14px;
  }
  .brand__dot {
    flex: none;
    width: 22px;
    height: 22px;
    border-radius: 50%;
    background: var(--text-lime);
  }
  .brand__name {
    margin: 0;
    font-size: 44px;
    line-height: 1.1;
    font-weight: 700;
    color: var(--text-yellow);
  }
  .divider {
    position: absolute;
    left: 470px;
    top: 70px;
    width: 2px;
    height: 250px;
    background: var(--swoosh-mid);
    opacity: .7;
  }
  .contact {
    position: absolute;
    left: 520px;
    top: 78px;
  }
  .contact__name {
    margin: 0;
    font-size: 42px;
    font-weight: 400;
    color: var(--text-white);
  }
  .contact__role {
    margin: 2px 0 14px;
    font-size: 24px;
    font-weight: 700;
    color: var(--text-lime);
  }
  .contact__line {
    display: flex;
    align-items: flex-start;
    gap: 10px;
    margin: 4px 0;
    font-size: 26px;
    line-height: 1.3;
    color: var(--text-yellow);
  }
  .contact__icon {
    flex: none;
    width: 22px;
    height: 22px;
    margin-top: 6px;
  }
  .grass {
    position: absolute;
    left: 0;
    right: 0;
    bottom: 52px;
    height: 90px;
    background: linear-gradient(to bottom, rgba(79,154,52,0), var(--grass-top) 55%, var(--grass-bottom));
  }
  .services {
    position: absolute;
    left: 0;
    right: 0;
    bottom: 0;
    height: 52px;
    background: var(--swoosh-mid);
    color: var(--footer-text);
    font-size: 24px;
    line-height: 52px;
    text-align: center;
    margin: 0;
  }
</style>
</head>
<body>
  <article class="card">
    <svg class="card__shapes" width="1000" height="570" viewBox="0 0 1000 570" aria-hidden="true">
      <path d="M0 0 H150 C60 120 40 300 90 570 H0 Z" fill="var(--swoosh-light)"/>
      <path d="M150 0 H200 C100 130 80 320 140 570 H90 C40 300 60 120 150 0 Z" fill="var(--swoosh-mid)"/>
    </svg>

    <div class="brand">
      <span class="brand__dot"></span>
      <p class="brand__name">Fern Hollow Lawn &amp; Garden</p>
    </div>

    <div class="divider"></div>

    <div class="contact">
      <h1 class="contact__name">deborah finch</h1>
      <p class="contact__role">Owner,operater</p>
      <div class="contact__line">
        <svg class="contact__icon" viewBox="0 0 22 22" aria-hidden="true">
          <circle cx="11" cy="11" r="11" fill="var(--text-lime)"/>
          <path d="M7 6 L9 6 L10 9 L8.6 10 C9.3 11.6 10.4 12.7 12 13.4 L13 12 L16 13 L16 15 C16 15.6 15.6 16 15 16 C10.6 16 6 11.4 6 7 C6 6.4 6.4 6 7 6 Z" fill="var(--card-dark)"/>
        </svg>
        <span>555-555-0147</span>
      </div>
      <div class="contact__line">
        <svg class="contact__icon" viewBox="0 0 22 22" aria-hidden="true">
          <circle cx="11" cy="11" r="11" fill="var(--text-lime)"/>
          <path d="M11 5 C8.5 5 7 6.8 7 9 C7 12 11 17 11 17 C11 17 15 12 15 9 C15 6.8 13.5 5 11 5 Z" fill="var(--card-dark)"/>
          <circle cx="11" cy="9" r="1.6" fill="var(--text-lime)"/>
        </svg>
        <span>2184 wexley millrd.e<br>cedarvale,tn. 38472</span>
      </div>
    </div>

    <div class="grass" role="img" aria-label="Grass blade strip along the lower edge of the card"></div>

    <p class="services">Residential,Commercial,Lawn and Landscape Maintenance, Bushhogging</p>
  </article>
</body>
</html>
```